Kestrel.vc needs a better website design!

We need a new and better website for Kestrel.vc. We're a Canadian venture capital firm that invests in innovative entrepreneurs. We compete against the following websites: lumora.vc, brightvalefund.ca, osprovc.com, and tessara.vc. We're a diverse group of partners and we're dedicated to the founders we invest in.
Updates

I don’t really like stock photos of random people as part of the website design…so please try to stay away from using those images. Thanks, Owen

Target Market(s)

Canadian entrepreneurs and investors

Industry/Entity Type

Venture capital, finance, investment, entrepreneurship

Coding

Coded - Design and coding required

Number of Pages Required

4 page

Font styles to use
Sans Serif

Colors

Designer to choose colors to be used in the design.

Requirements
Must have
• Clean crisp overall design. Fast and to the point.
Nice to have
• Check out www.kestrel.vc - I did it myself and it is too basic and too wordy.
Should not have
• No stock images with random people in them! Not too wordy or with too many large images that are slow to load.

```html
<!DOCTYPE html>
<html lang="en">
<head>
<meta charset="utf-8">
<title>Kestrel.vc — Venture Capital</title>
<link href="https://fonts.googleapis.com/css2?family=Poppins:wght@400;500;600&display=swap" rel="stylesheet">
<style>
:root{
  --green:#7b9b2f;
  --green-dark:#6f8d2a;
  --ink:#1f2412;
  --text:#2b2b2b;
  --muted:#5a5a5a;
  --line:#e3e3e3;
  --footer-bg:#f5f5f5;
  --white:#ffffff;
  --social:#1fb8e6;
}
*{margin:0;padding:0;box-sizing:border-box}
html,body{width:1200px;height:2294px;overflow:hidden;background:var(--white)}
body{font-family:"Poppins",sans-serif;color:var(--text);position:relative}
.site-header{position:absolute;top:0;left:0;width:1200px;height:114px;background:var(--white)}
.brand{position:absolute;left:162px;top:40px;display:flex;align-items:center;gap:8px;color:var(--green);font-weight:600;font-size:17px;letter-spacing:.5px}
.brand-dot{width:14px;height:14px;border-radius:50%;background:var(--green)}
.main-nav{position:absolute;top:48px;left:718px;display:flex;gap:0}
.main-nav a{font-size:14px;color:#444;text-decoration:none;margin-right:52px;padding-bottom:6px}
.main-nav a.active{color:var(--green);border-bottom:2px solid var(--green)}
.hero{position:absolute;top:114px;left:0;width:1200px;height:580px;background:linear-gradient(180deg,#6b6f66 0%,#4f5a46 30%,#3e5231 60%,#36501f 100%)}
.hero-title{position:absolute;top:138px;left:150px;width:900px;text-align:center;color:var(--white);font-weight:600;font-size:28.5px;line-height:47px}
.numbers-label{position:absolute;top:328px;left:0;width:1200px;text-align:center;color:var(--white);font-size:19px}
.numbers-rule{position:absolute;top:343px;height:1px;background:rgba(255,255,255,.35);width:210px}
.stat{position:absolute;top:375px;width:165px;height:60px;border:1px solid rgba(255,255,255,.55);display:flex;align-items:center;justify-content:center;gap:7px;color:var(--white)}
.stat-num{font-size:36px;font-weight:500;line-height:1}
.stat-label{font-size:14px;line-height:15px;font-weight:500}
.hero-wave{position:absolute;top:590px;left:0}
.intro-title{position:absolute;top:724px;left:0;width:1200px;text-align:center;font-size:27px;font-weight:600;color:var(--ink);line-height:42px}
.service-card{position:absolute;top:845px;width:420px;height:269px;border:1px solid #dcdcdc;border-radius:4px;background:var(--white);box-shadow:0 2px 10px rgba(0,0,0,.06);padding:48px 30px 0 34px}
.service-card p{position:absolute;top:140px;left:34px;right:18px;font-size:20px;line-height:32.5px;color:var(--text)}
.icon-placeholder{width:72px;height:76px;background:#e8ecdf;border-radius:6px}
.portfolio-title{position:absolute;top:1200px;left:0;width:1200px;text-align:center;font-size:27px;font-weight:600;color:var(--ink)}
.logo-tile{position:absolute;width:154px;height:67px;border:1px solid #ececec;border-radius:3px;box-shadow:0 1px 6px rgba(0,0,0,.06);display:flex;align-items:center;justify-content:center;font-size:17px;font-weight:600;color:#333;background:var(--white)}
.cta{position:absolute;top:1527px;left:0;width:1200px;height:450px;background:linear-gradient(135deg,#7f9f33 0%,#769630 50%,#80a036 100%)}
.cta-title{position:absolute;top:135px;left:207px;font-size:52px;font-weight:500;line-height:64px;color:var(--white)}
.cta-sub{position:absolute;top:268px;left:207px;font-size:27px;color:var(--white)}
.site-footer{position:absolute;top:1977px;left:0;width:1200px;height:273px;background:var(--footer-bg)}
.footer-brand{position:absolute;left:162px;top:178px;display:flex;align-items:center;gap:10px;color:var(--green);font-size:30px;font-weight:600}
.footer-brand .brand-dot{width:26px;height:26px}
.footer-heading{font-size:20px;font-weight:500;color:var(--ink)}
.quick-links{position:absolute;left:544px;top:58px}
.quick-links ul{list-style:none;margin-top:12px}
.quick-links li{font-size:14px;line-height:32.5px;color:#333}
.quick-links li::before{content:"›";margin-right:9px;color:#555}
.contact{position:absolute;left:852px;top:58px}
.contact-row{margin-top:14px;font-size:14px;color:#333}
.contact-row b{font-weight:600;margin-right:34px}
.follow{margin-top:26px}
.social{display:flex;gap:7px;margin-top:10px}
.social span{width:31px;height:31px;border-radius:50%;background:var(--social)}
.social span+span{background:#1a9ed6}
.copyright{position:absolute;top:2250px;left:0;width:1200px;height:44px;background:var(--green);color:var(--white);font-size:14px;font-weight:500;text-align:center;line-height:44px}
</style>
</head>
<body>
<header class="site-header">
  <div class="brand"><span class="brand-dot"></span>KESTREL.VC</div>
  <nav class="main-nav">
    <a href="#" class="active">Home</a>
    <a href="#">What</a>
    <a href="#">Who</a>
    <a href="#">Portfolio</a>
  </nav>
</header>

<section class="hero" role="img" aria-label="Misty green mountain valley landscape photograph">
  <h1 class="hero-title">Kestrel.vc is a venture capital firm that invests in innovative seed-stage technology companies in Western Canada focused on B2B and SaaS markets.</h1>
  <div class="numbers-rule" style="left:262px"></div>
  <div class="numbers-label">Kestrel.vc in numbers</div>
  <div class="numbers-rule" style="left:723px"></div>
  <div class="stat" style="left:333px"><span class="stat-num">10</span><span class="stat-label">Portfolio<br>companies</span></div>
  <div class="stat" style="left:517px"><span class="stat-num">7</span><span class="stat-label">Follow-on<br>financings</span></div>
  <div class="stat" style="left:701px"><span class="stat-num">100</span><span class="stat-label">+<br>Employees</span></div>
</section>
<svg class="hero-wave" width="1200" height="110" viewBox="0 0 1200 110" aria-hidden="true">
  <path d="M0 60 C120 18 220 10 330 14 C470 20 560 90 720 96 C880 102 1050 90 1200 56 L1200 110 L0 110 Z" fill="#ffffff"/>
</svg>

<h2 class="intro-title">We are serial entrepreneurs and venture<br>capital investors who provide</h2>

<article class="service-card" style="left:161px">
  <svg width="80" height="76" viewBox="0 0 80 76" aria-hidden="true">
    <rect x="1" y="58" width="12" height="17" fill="none" stroke="#888" stroke-width="2"/>
    <rect x="21" y="44" width="12" height="31" fill="none" stroke="#888" stroke-width="2"/>
    <rect x="41" y="30" width="12" height="45" fill="none" stroke="#888" stroke-width="2"/>
    <rect x="61" y="12" width="12" height="63" fill="none" stroke="#888" stroke-width="2"/>
    <path d="M3 34 C22 30 40 20 55 2" fill="none" stroke="var(--green)" stroke-width="2.5"/>
    <path d="M47 3 L56 1 L55 10" fill="none" stroke="var(--green)" stroke-width="2.5"/>
  </svg>
  <p>Mentoring and strategic advice to help you grow your company quickly and efficiently</p>
</article>
<article class="service-card" style="left:619px">
  <div class="icon-placeholder" role="img" aria-label="Investor with dollar coin icon"></div>
  <p>Investor introductions to help you raise additional follow-on funding for your startup</p>
</article>

<h2 class="portfolio-title">Check out our innovative portfolio companies!</h2>
<div class="logo-tile" style="left:161px;top:1276px">Brightwave</div>
<div class="logo-tile" style="left:342px;top:1276px">ledgerly</div>
<div class="logo-tile" style="left:523px;top:1276px">Calmpath</div>
<div class="logo-tile" style="left:703px;top:1276px">Opsline</div>
<div class="logo-tile" style="left:884px;top:1276px">Noventa</div>
<div class="logo-tile" style="left:161px;top:1364px">Tallyo</div>
<div class="logo-tile" style="left:342px;top:1364px">Gamerift</div>
<div class="logo-tile" style="left:523px;top:1364px">Keystone Entry</div>
<div class="logo-tile" style="left:703px;top:1364px">Homefold</div>
<div class="logo-tile" style="left:884px;top:1364px">Nutrafit</div>

<section class="cta">
  <h2 class="cta-title">If you have what<br>we're looking for</h2>
  <p class="cta-sub">Contact us today</p>
</section>

<footer class="site-footer">
  <div class="footer-brand" style="top:170px"><span class="brand-dot"></span>KESTREL.VC</div>
  <div class="quick-links">
    <h3 class="footer-heading">Quick Links</h3>
    <ul><li>Home</li><li>What</li><li>Who</li><li>Portfolio</li></ul>
  </div>
  <div class="contact">
    <h3 class="footer-heading">Get In Touch</h3>
    <p class="contact-row"><b>Email:</b>hello@kestrel.vc</p>
    <h3 class="footer-heading follow">Follow Us</h3>
    <div class="social"><span role="img" aria-label="Social profile one"></span><span role="img" aria-label="Social profile two"></span></div>
  </div>
</footer>
<div class="copyright">Copyright © 2021 Kestrel.vc - All Rights Reserved.</div>
</body>
</html>
```